Business Card for Trivelo, a french tech company

Tech company
New technologies
Serious design
Dark theme

User info :
Name: Florian GASTIER
Position: Co-Founder & CEO
Tel: (+33) 6 52 84 26 07
Email: florian@trivelo.example
Website: www.trivelo.example
Address: 17 rue des Tanneurs 69001 LYON

```html
<!DOCTYPE html>
<html lang="en">
<head>
<meta charset="utf-8">
<title>Trivelo – Business Card</title>
<link rel="stylesheet" href="https://fonts.googleapis.com/css2?family=Montserrat:wght@700&family=Open+Sans:wght@400;700&display=swap">
<style>
  :root {
    --page-bg: #121319;
    --card-bg: #1d1f29;
    --card-edge: #2e3140;
    --accent: #d6287f;
    --brand: #c23d8e;
    --ink: #e6e4ea;
    --ink-soft: #b9b7c4;
  }
  * { margin: 0; padding: 0; box-sizing: border-box; }
  html, body {
    width: 1200px;
    height: 1047px;
    overflow: hidden;
    background: var(--page-bg);
  }
  .card {
    position: absolute;
    left: 100px;
    top: 251px;
    width: 1000px;
    height: 545px;
    background: var(--card-bg);
    border: 2px solid var(--card-edge);
    border-radius: 20px;
    box-shadow: 0 12px 36px rgba(0, 0, 0, 0.45);
    font-family: "Open Sans", sans-serif;
    color: var(--ink);
  }
  .brand-name {
    position: absolute;
    left: 85px;
    top: 232px;
    width: 437px;
    text-align: center;
    font-family: "Montserrat", sans-serif;
    font-weight: 700;
    font-size: 74px;
    line-height: 80px;
    letter-spacing: 3px;
    color: var(--brand);
  }
  .divider {
    position: absolute;
    left: 576px;
    top: 131px;
    width: 3px;
    height: 283px;
    background: var(--accent);
  }
  .identity {
    position: absolute;
    left: 623px;
    top: 124px;
  }
  .person-name {
    font-weight: 700;
    font-size: 34px;
    line-height: 46px;
    color: var(--accent);
    white-space: nowrap;
  }
  .person-role {
    font-size: 24px;
    line-height: 32px;
    color: var(--ink-soft);
  }
  .contact-list {
    position: absolute;
    left: 623px;
    top: 225px;
    list-style: none;
  }
  .contact-item {
    display: flex;
    align-items: center;
    gap: 10px;
    font-size: 23px;
    line-height: 33px;
    white-space: nowrap;
  }
  .contact-icon {
    width: 22px;
    height: 22px;
    fill: var(--accent);
    flex: none;
  }
  .address {
    position: absolute;
    left: 623px;
    top: 352px;
    font-size: 23px;
    line-height: 32px;
    font-style: normal;
    white-space: nowrap;
  }
</style>
</head>
<body>
  <div class="card">
    <div class="brand-name">Trivelo</div>

    <div class="divider"></div>

    <div class="identity">
      <div class="person-name">Florian GASTIER</div>
      <div class="person-role">Co-Founder &amp; CEO</div>
    </div>

    <ul class="contact-list">
      <li class="contact-item">
        <svg class="contact-icon" viewBox="0 0 24 24" aria-hidden="true">
          <path d="M6.6 10.8a15.1 15.1 0 0 0 6.6 6.6l2.2-2.2a1 1 0 0 1 1-.25 11.4 11.4 0 0 0 3.6.57 1 1 0 0 1 1 1V20a1 1 0 0 1-1 1A17 17 0 0 1 3 4a1 1 0 0 1 1-1h3.5a1 1 0 0 1 1 1c0 1.25.2 2.45.57 3.6a1 1 0 0 1-.25 1z"/>
        </svg>
        (+33) 6 52 84 26 07
      </li>
      <li class="contact-item">
        <svg class="contact-icon" viewBox="0 0 24 24" aria-hidden="true">
          <path d="M3 6h18v1.2l-9 5.6-9-5.6z"/>
          <path d="M3 9.4l9 5.6 9-5.6V18H3z"/>
        </svg>
        florian@trivelo.example
      </li>
      <li class="contact-item">
        <svg class="contact-icon" viewBox="0 0 24 24" aria-hidden="true">
          <path d="M12 2a10 10 0 1 0 0 20 10 10 0 0 0 0-20zm-1 17.9A8 8 0 0 1 4.1 10L9 15v1a2 2 0 0 0 2 2zm6.9-2.5A2 2 0 0 0 16 16h-1v-3a1 1 0 0 0-1-1H8v-2h2a1 1 0 0 0 1-1V7h2a2 2 0 0 0 2-2v-.4a8 8 0 0 1 2.9 12.8z"/>
        </svg>
        www.trivelo.example
      </li>
    </ul>

    <address class="address">
      17 rue des Tanneurs<br>
      69001 LYON
    </address>
  </div>
</body>
</html>
```